Telecommunications/Power civil contractor needs business card design

Were a new telecommunications/power underground civil contractor that is looking for a new business card design. Our company colours are silver or grey and orange. Feel free to use the white background logo or the black background logo.

Target Market(s)

Local contractors, utility companies, private sector mining/energy companies, developers.

Industry/Entity Type

Telecommunications

Contact Information for Business Card

Each card will need the following info:
Persons name:
Title:
E-mail:
Phone number:
Shop Address:
Mailing Address:

Requirements
Must have
• Each card will need the following info:
• Persons name:
• Title:
• E-mail:
• Phone number:
• Shop Address:
• Mailing Address:

```html
<!DOCTYPE html>
<html lang="en">
<head>
<meta charset="utf-8">
<title>Trenchline Utility Works Inc — Business Card</title>
<link rel="stylesheet" href="https://fonts.googleapis.com/css2?family=Open+Sans:wght@600;700&family=Russo+One&display=swap">
<style>
  :root {
    --page: #ffffff;
    --card-dark: #1c1c1d;
    --card-mid: #2e2e31;
    --accent-orange: #f0642a;
    --logo-grey: #8e8e91;
    --text-light: #ffffff;
    --text-soft: #c9c9cc;
  }
  html, body {
    margin: 0;
    padding: 0;
    width: 1200px;
    height: 739px;
    overflow: hidden;
    background: var(--page);
  }
  .canvas {
    position: relative;
    width: 1200px;
    height: 739px;
  }
  .business-card {
    position: absolute;
    left: 340px;
    top: 220px;
    width: 601px;
    height: 321px;
    overflow: hidden;
    background: var(--card-dark);
  }
  .card-backdrop {
    position: absolute;
    inset: 0;
  }
  .brand-circle {
    position: absolute;
    left: 81px;
    top: 55px;
    width: 80px;
    height: 80px;
    border: 4px solid var(--logo-grey);
    border-radius: 50%;
    box-sizing: border-box;
  }
  .brand-name {
    position: absolute;
    left: 41px;
    width: 160px;
    margin: 0;
    font-family: "Russo One", sans-serif;
    color: var(--accent-orange);
    text-align: center;
    white-space: nowrap;
  }
  .brand-name--main { top: 147px; font-size: 22px; line-height: 24px; letter-spacing: 0.5px; }
  .brand-name--sub { top: 173px; font-size: 9px; line-height: 11px; letter-spacing: 0.6px; }
  .holder {
    position: absolute;
    left: 41px;
    top: 214px;
    margin: 0;
    font-family: "Open Sans", sans-serif;
    color: var(--text-light);
    white-space: nowrap;
  }
  .holder__name { margin: 0; font-size: 13px; line-height: 18px; font-weight: 700; }
  .holder__title { margin: 0; font-size: 10px; line-height: 14px; font-weight: 600; color: var(--accent-orange); }
  .title-band {
    position: absolute;
    left: 337px;
    top: 127px;
    color: var(--text-light);
    font-family: "Russo One", sans-serif;
    white-space: nowrap;
  }
  .title-band__name { margin: 0; font-size: 33px; line-height: 36px; font-weight: 400; letter-spacing: 0.5px; }
  .title-band__sub { margin: 0; font-size: 13.5px; line-height: 17px; letter-spacing: 0.6px; }
  .contact-list {
    position: absolute;
    left: 249px;
    top: 204px;
    margin: 0;
    padding: 0;
    list-style: none;
    font-family: "Open Sans", sans-serif;
    font-weight: 700;
    font-size: 12px;
    color: var(--text-light);
  }
  .contact-item {
    display: flex;
    align-items: center;
    height: 21px;
    white-space: nowrap;
  }
  .contact-icon {
    width: 14px;
    height: 14px;
    margin-right: 19px;
    flex: none;
  }
</style>
</head>
<body>
<main class="canvas">
  <section class="business-card">
    <svg class="card-backdrop" width="601" height="321" viewBox="0 0 601 321">
      <defs>
        <radialGradient id="glow" cx="0.55" cy="0.05" r="0.75">
          <stop offset="0" stop-color="#2f2f32"/>
          <stop offset="1" stop-color="#1d1d1f"/>
        </radialGradient>
        <linearGradient id="edge-shadow" x1="0" y1="0" x2="1" y2="0">
          <stop offset="0" stop-color="#000" stop-opacity="0"/>
          <stop offset="1" stop-color="#000" stop-opacity="0.4"/>
        </linearGradient>
      </defs>
      <rect width="601" height="321" fill="url(#glow)"/>
      <polygon points="0,0 423,0 84,321 0,321" fill="#1c1c1d"/>
      <polygon points="400,0 423,0 84,321 62,321" fill="url(#edge-shadow)"/>
      <polygon points="301,117 601,117 601,194 216,194" fill="var(--accent-orange)"/>
    </svg>

    <span class="brand-circle"></span>
    <p class="brand-name brand-name--main">TRENCHLINE</p>
    <p class="brand-name brand-name--sub">UTILITY WORKS INC</p>

    <div class="holder">
      <p class="holder__name">Jordan Reyes</p>
      <p class="holder__title">Operations Manager</p>
    </div>

    <div class="title-band">
      <h1 class="title-band__name">TRENCHLINE</h1>
      <p class="title-band__sub">UTILITY WORKS INC</p>
    </div>

    <ul class="contact-list">
      <li class="contact-item">
        <svg class="contact-icon" viewBox="0 0 15 15"><rect width="15" height="15" fill="#fff"/><rect x="5" y="2.5" width="5" height="10" rx="1" fill="#1c1c1d"/><rect x="6" y="4" width="3" height="6" fill="#fff"/></svg>
        phone: +0001 6912036
      </li>
      <li class="contact-item">
        <svg class="contact-icon" viewBox="0 0 15 15"><rect width="15" height="15" fill="#fff"/><rect x="2.5" y="3.5" width="10" height="7" fill="#1c1c1d"/><rect x="3.5" y="4.5" width="8" height="5" fill="#fff"/><rect x="2.5" y="11" width="10" height="1" fill="#1c1c1d"/></svg>
        e-mail: youremail@email.com
      </li>
      <li class="contact-item">
        <svg class="contact-icon" viewBox="0 0 15 15"><rect width="15" height="15" fill="#fff"/><g fill="none" stroke="#1c1c1d" stroke-width="0.9"><circle cx="7.5" cy="7.5" r="4.5"/><ellipse cx="7.5" cy="7.5" rx="2" ry="4.5"/><line x1="3" y1="7.5" x2="12" y2="7.5"/><line x1="7.5" y1="3" x2="7.5" y2="12"/></g></svg>
        website: www.yoursite.com
      </li>
      <li class="contact-item">
        <svg class="contact-icon" viewBox="0 0 15 15"><rect width="15" height="15" fill="#fff"/><path d="M7.5 2.5a3.5 3.5 0 0 1 3.5 3.5c0 2.6-3.5 6.5-3.5 6.5S4 8.6 4 6a3.5 3.5 0 0 1 3.5-3.5z" fill="#1c1c1d"/><circle cx="7.5" cy="6" r="1.3" fill="#fff"/></svg>
        shop: 1480 Quarry Road, Red Deer AB
      </li>
      <li class="contact-item">
        <svg class="contact-icon" viewBox="0 0 15 15"><rect width="15" height="15" fill="#fff"/><rect x="2.5" y="4" width="10" height="7" fill="#1c1c1d"/><polyline points="3,4.5 7.5,8 12,4.5" fill="none" stroke="#fff" stroke-width="0.9"/></svg>
        mailing: PO Box 2217, Red Deer AB
      </li>
    </ul>
  </section>
</main>
</body>
</html>
```